logo & Business Card Design

BrightHaven Termite & Pest Control, I need a great logo, take my ideas and run with them!
I will use this in marketing and website so needs to be eye catching but professional

Target Market(s)

Resedintial & Business

Industry/Entity Type

Marketing

Contact Information for Business Card

Need front side with pertinent info & Logo; back side will have a 25% off initial services Coupon!

Font styles to use
Sans Serif

Colors
ec1f27
1b1b1b

Requirements
Must have
• Professional logo and style
Nice to have
• Raised lettering, black, red, white colors maybe? I'm flexible, but those colors go good on any background, vehicle, uniform, etc...
Should not have
• Cheesy

```html
<!DOCTYPE html>
<html lang="en">
<head>
<meta charset="UTF-8">
<title>BrightHaven Termite &amp; Pest Control – Business Card</title>
<link href="https://fonts.googleapis.com/css2?family=Libre+Baskerville:wght@700&family=Open+Sans:wght@400;600&display=swap" rel="stylesheet">
<style>
  :root {
    --backdrop: #e9e6e2;
    --card-black: #0c0c0c;
    --panel-black: #111111;
    --paper: #ffffff;
    --ink: #1b1b1b;
    --accent: #d2481f;
    --accent-deep: #b83a17;
    --text-light: #f2f2f2;
    --rule: #8a8a8a;
    --mark-grey: #c9ccd1;
  }
  * { margin: 0; padding: 0; box-sizing: border-box; }
  html, body {
    width: 1200px; height: 915px; overflow: hidden;
    background: var(--backdrop);
    font-family: "Open Sans", Arial, sans-serif;
  }
  .stage {
    position: relative; width: 1200px; height: 915px;
    display: flex; justify-content: center; align-items: center; gap: 40px;
  }
  .card {
    position: relative; width: 440px; height: 700px;
    border-radius: 26px; overflow: hidden;
    box-shadow: 0 10px 26px rgba(0,0,0,0.25);
  }

  /* Back side */
  .card-back {
    background: var(--card-black);
    display: flex; justify-content: center; align-items: center;
  }
  .brand-mark {
    display: flex; align-items: center; gap: 12px;
    font-family: "Open Sans", Arial, sans-serif; font-weight: 600;
    font-size: 30px; line-height: 1.3;
  }
  .brand-mark .dot {
    width: 26px; height: 26px; border-radius: 50%;
    flex-shrink: 0;
  }
  .card-back .brand-mark { color: var(--mark-grey); }
  .card-back .brand-mark .dot { background: var(--accent); }

  /* Front side */
  .card-front { background: var(--panel-black); }
  .front-top {
    height: 318px; background: var(--paper);
    display: flex; flex-direction: column; align-items: center;
    padding-top: 72px;
  }
  .card-front .brand-mark { color: var(--ink); font-size: 34px; }
  .card-front .brand-mark .dot { background: var(--accent); }
  .company-name {
    margin-top: 66px;
    font-family: "Libre Baskerville", Georgia, serif; font-weight: 700;
    color: var(--ink); font-size: 33px; letter-spacing: 1px; line-height: 1;
  }
  .company-tagline {
    margin-top: 8px;
    font-family: "Libre Baskerville", Georgia, serif; font-weight: 700;
    color: var(--ink); font-size: 19px; letter-spacing: 0.5px; line-height: 1.3;
  }
  .front-details { padding: 22px 40px 0 62px; color: var(--text-light); }
  .person-name { color: var(--accent); font-size: 31px; line-height: 1.1; }
  .person-role { font-size: 20px; line-height: 1.35; margin-top: 2px; }
  .divider { height: 1px; background: var(--rule); margin: 12px 0 14px; width: 290px; }
  .address { font-size: 20px; line-height: 1.35; }
  .contact-list { list-style: none; }
  .contact-list li {
    display: flex; align-items: center; gap: 14px;
    font-size: 17px; line-height: 24px; margin-bottom: 6px;
  }
  .contact-icon {
    width: 22px; height: 22px; border: 1.5px solid var(--text-light);
    border-radius: 50%; display: flex; align-items: center; justify-content: center;
    flex-shrink: 0;
  }
  .contact-icon svg { width: 12px; height: 12px; fill: none; stroke: var(--text-light); stroke-width: 1.8; }
  .footer-band {
    position: absolute; left: 0; right: 0; bottom: 0; height: 42px;
    background: linear-gradient(var(--accent), var(--accent-deep));
    border-top: 6px solid var(--paper);
  }
</style>
</head>
<body>
<main class="stage">
  <section class="card card-back" aria-label="Card back">
    <div class="brand-mark"><span class="dot"></span>BrightHaven</div>
  </section>

  <section class="card card-front" aria-label="Card front">
    <header class="front-top">
      <div class="brand-mark"><span class="dot"></span>BrightHaven</div>
      <h1 class="company-name">BRIGHTHAVEN</h1>
      <p class="company-tagline">TERMITE &amp; PEST CONTROL</p>
    </header>
    <div class="front-details">
      <p class="person-name">Your Name</p>
      <p class="person-role">Managing Director</p>
      <div class="divider"></div>
      <p class="address">Suite 5, 210 Harbour Road<br>Kelvale, VIC 3090</p>
      <div class="divider"></div>
      <ul class="contact-list">
        <li><span class="contact-icon"><svg viewBox="0 0 12 12"><path d="M2 1.5l2 .2.8 2.3-1.2 1a6 6 0 0 0 3.4 3.4l1-1.2 2.3.8.2 2A1 1 0 0 1 9.5 11 9 9 0 0 1 1 2.5a1 1 0 0 1 1-1z"/></svg></span>+61 3 9555 0148</li>
        <li><span class="contact-icon"><svg viewBox="0 0 12 12"><rect x="3" y="1" width="6" height="10" rx="1"/><path d="M5 9h2"/></svg></span>+61 400 555 237</li>
        <li><span class="contact-icon"><svg viewBox="0 0 12 12"><rect x="1" y="2.5" width="10" height="7"/><path d="M1 2.5l5 4 5-4"/></svg></span>info@brighthavenpest.com</li>
        <li><span class="contact-icon"><svg viewBox="0 0 12 12"><circle cx="6" cy="6" r="5"/><path d="M1 6h10M6 1c-2.5 3-2.5 7 0 10M6 1c2.5 3 2.5 7 0 10"/></svg></span>www.brighthavenpest.com</li>
      </ul>
    </div>
    <div class="footer-band"></div>
  </section>
</main>
</body>
</html>
```